Stella Marina packaging design

Hi there,
I'm trying to get an outstanding and unique design for my new product.I'm in baby products business.We are launching an organic,100% burp cloth for our online store. The packaging design is very important to our business.We are looking for something simple and unique.Our brand name is Stella Marina which means Sea Star in Italian. We also have dolphin prints on the burp cloth. Our burp cloth made of organic, hypoallergenic, breathable and ultra soft 100% cotton.Each box has 5 burp cloth. Its made with love and care for delicate and sensitive baby skin.I will attach samples of the burp cloth colors for you to get an idea about the product.

baby product

• Our Logo, ORVA image , and made of organic, hypoallergenic, breathable and ultra soft 100% cotton,has 5 burp cloth. Its made with love and care for delicate and sensitive baby skin.I will attach samples of the burp cloth colors for you to get an idea about the product.
• We are looking for something different and can Standout , please to don't make design that has the exact idea of the template that I provide.

```html
<!DOCTYPE html>
<html lang="en">
<head>
<meta charset="utf-8">
<title>Stella Marina – Baby Burp Cloth box</title>
<link rel="stylesheet" href="https://fonts.googleapis.com/css2?family=Fredoka:wght@600&family=Quicksand:wght@400;500;600&display=swap">
<style>
  :root{
    --ink:#555a5e;
    --ink-soft:#6d7174;
    --brand-grey:#5e5f61;
    --sky:#bfe2ec;
    --sky-box:#b7dee8;
    --sky-faint:#e4f4fa;
    --blush:#f1c3ce;
    --blush-deep:#e9a9b9;
    --berry:#a3327e;
    --seal:#3fae5a;
    --line:#4d4d4d;
    --paper:#ffffff;
  }
  *{box-sizing:border-box;margin:0;padding:0}
  html,body{width:1200px;height:555px;overflow:hidden;background:var(--paper)}
  body{font-family:"Quicksand",sans-serif;color:var(--ink)}
  .canvas{position:relative;width:1200px;height:555px;overflow:hidden;background:var(--paper);border:1px solid #cfcfcf}
  .abs{position:absolute}

  .wash{position:absolute}
  .wash--flap{left:300px;top:48px;width:216px;height:129px;
    background:radial-gradient(ellipse at 45% 40%,var(--sky-faint) 0%,var(--sky-faint) 55%,rgba(228,244,250,0) 75%)}
  .wash--front{left:83px;top:340px;width:190px;height:126px;
    background:radial-gradient(ellipse at 35% 60%,#eef8fc 0%,#eef8fc 50%,rgba(238,248,252,0) 75%)}

  .dieline{position:absolute;left:0;top:0}

  .brand{display:flex;align-items:center;gap:6px;font-family:"Quicksand",sans-serif;font-weight:600;color:var(--brand-grey)}
  .brand__dot{width:12px;height:12px;border-radius:50%;background:var(--brand-grey)}
  .brand--front{left:229px;top:226px;font-size:18px}
  .brand--flap{left:236px;top:122px;font-size:15px;transform:rotate(180deg)}

  .title{font-family:"Fredoka",sans-serif;font-weight:600;color:var(--sky);letter-spacing:.5px}
  .title--front{left:82px;width:434px;top:293px;text-align:center;font-size:34px}
  .subtitle{font-family:"Quicksand",sans-serif;font-weight:500;color:var(--ink)}
  .subtitle--front{left:82px;width:434px;top:339px;text-align:center;font-size:15px}

  .features{left:166px;top:381px;list-style:none;font-size:7.4px;letter-spacing:.3px;color:var(--ink)}
  .features li{display:flex;align-items:center;gap:6px;height:11.5px}
  .features__icon{width:7px;height:7px;border:0.8px solid var(--blush-deep);border-radius:50%}

  .product-shot{left:358px;top:366px;width:90px;height:78px;border-radius:3px;
    background:linear-gradient(135deg,var(--blush) 0%,#f7dbe3 45%,#d9eff5 100%);transform:rotate(-4deg)}

  .seal{left:101px;top:446px;width:38px;height:38px;border-radius:50%;background:var(--seal)}

  .band-blush{left:82px;top:467px;width:434px;height:6px;background:var(--blush)}
  .band-grey{left:82px;top:473px;width:434px;height:16px;background:var(--brand-grey);
    color:#fff;font-size:8px;text-align:center;line-height:16px;letter-spacing:.4px}

  .count{left:438px;top:446px;width:48px;height:43px;background:var(--sky-box);color:#fff;text-align:center}
  .count__num{font-family:"Fredoka",sans-serif;font-size:20px;line-height:26px}
  .count__label{font-size:7px;line-height:9px}

  .spine{display:flex;flex-direction:column;align-items:center;transform:rotate(-90deg);transform-origin:center}
  .spine__title{font-family:"Fredoka",sans-serif;font-weight:600;color:var(--sky);font-size:21px;white-space:nowrap;line-height:26px}
  .spine__sub{font-size:10px;color:var(--ink);white-space:nowrap;line-height:14px;align-self:flex-end}
  .spine--left{left:477px;top:320px;width:210px}
  .spine--right{left:1016px;top:320px;width:210px}

  .story{left:641px;width:400px;font-size:8.6px;line-height:12.6px;color:var(--ink)}
  .story--intro{top:197px}
  .story--bamboo{top:246px}

  .care{left:641px;top:304px;width:134px;height:115px;background:var(--sky-box);border-radius:8px;color:#fff;padding:9px 13px}
  .care__heading{font-size:11px;font-weight:500;letter-spacing:.2px;margin-bottom:2px}
  .care__list{list-style:none;font-size:10.4px;line-height:14px}
  .care__list li::before{content:"•";margin-right:7px}

  .tips{left:781px;top:312px;width:260px}
  .tips__heading{font-size:6.8px;color:var(--berry);font-weight:600;letter-spacing:.2px}
  .tips__list{list-style:none;font-size:6.3px;line-height:8.4px;color:var(--ink-soft)}
  .tips__list li{padding-left:7px;position:relative}
  .tips__list li::before{content:"•";position:absolute;left:0}

  .laundry{left:641px;top:459px}
  .origin{left:739px;top:457px;font-size:6.6px;line-height:9px;color:var(--ink)}
  .sku{left:896px;top:455px;font-size:8px;line-height:10px;color:#222}
</style>
</head>
<body>
<main class="canvas">

  <div class="wash wash--flap" role="img" aria-label="Faint sky-blue sea creature illustration on the lid"></div>
  <div class="wash wash--front" role="img" aria-label="Faint pale-blue sea creature illustration in the lower corner"></div>

  <svg class="dieline" width="1200" height="555" viewBox="0 0 1200 555" fill="none" stroke="var(--line)" stroke-width="1">
    <path d="M82 177 V60 Q82 47 96 47 H502 Q516 47 516 60 V177"/>
    <path d="M82 73 H516"/>
    <path d="M82 177 L50 187 V480 L82 489"/>
    <rect x="82" y="177" width="434" height="312"/>
    <rect x="516" y="177" width="103" height="312"/>
    <rect x="619" y="177" width="434" height="312"/>
    <rect x="1053" y="177" width="104" height="312"/>
    <path d="M530 177 V113 Q530 107 536 107 H606 L612 148 L619 150"/>
    <path d="M1065 177 V150 L1072 148 L1078 107 H1116 Q1122 107 1122 113 V177"/>
  </svg>

  <!-- Lid -->
  <div class="abs brand brand--flap"><span class="brand__dot"></span>Stella Marina</div>

  <!-- Front panel -->
  <div class="abs brand brand--front"><span class="brand__dot"></span>Stella Marina</div>
  <h1 class="abs title title--front">Baby Burp Cloth</h1>
  <p class="abs subtitle subtitle--front">100%organic</p>

  <ul class="abs features">
    <li><span class="features__icon"></span>UNBLEACHED, CHEMICAL &amp; TOXIN FREE</li>
    <li><span class="features__icon"></span>THREE TIMES MORE ABSORBENT THAN COTTON</li>
    <li><span class="features__icon"></span>HYPOALLERGENIC AND ANTIBACTERIAL</li>
    <li><span class="features__icon"></span>ECO FRIENDLY AND ULTRA SOFT 100% COTTON</li>
  </ul>

  <div class="abs product-shot" role="img" aria-label="Fanned stack of pink and white patterned burp cloths"></div>
  <div class="abs seal" role="img" aria-label="Organic textile certification badge"></div>

  <div class="abs band-blush"></div>
  <div class="abs band-grey">25*22*3.5cm.</div>
  <div class="abs count"><div class="count__num">5</div><div class="count__label">burp cloth</div></div>

  <!-- Side panels -->
  <div class="abs spine spine--left"><span class="spine__title">Baby Burp Cloth</span><span class="spine__sub">100%organic</span></div>
  <div class="abs spine spine--right"><span class="spine__title">Baby Burp Cloth</span><span class="spine__sub">100%organic</span></div>

  <!-- Back panel -->
  <p class="abs story story--intro">Do you ever find yourself questioning what products are best for your little one? We thought so. We are here at Stella Marina , and nothing is more important to us than the well-being of our little ones.</p>
  <p class="abs story story--bamboo">100% organic bamboo is the best of the best for our bundles of joy, being ultra soft, antibacterial, hypoallergenic, free of dyes &amp; chemicals, and 3x more absorbent than cotton. These dreamy towels will leave your baby cozy, dry, and happily wrapped up in a silky soft embrace after bath time. From our mama hearts, to yours</p>

  <section class="abs care">
    <h2 class="care__heading">CARE INSTRUCTIONS</h2>
    <ul class="care__list">
      <li>Machine Wash</li>
      <li>Hand Wash</li>
      <li>Do not Dry Clean</li>
      <li>Do not Bleach</li>
      <li>Do not Tumble Dry</li>
    </ul>
  </section>

  <section class="abs tips">
    <h3 class="tips__heading">ADDITIONAL CARE TIPS</h3>
    <ul class="tips__list">
      <li>Wash before first use</li>
      <li>Do not store wet bath towel</li>
      <li>Store in a well aired room (never in a sealed container, plastic bag, etc)<br>Avoid contact with rough surfaces which could loosen the yarns</li>
      <li>Do not bleach or use fabric softeners. Dryer sheets are also not recommended</li>
      <li>Keep away from open flames or electric heaters</li>
      <li>If towel is used after swimming pools, sea water, chlorinated water, please be sure to wash immediately after to prevent the bamboo fibre from weakening</li>
    </ul>
  </section>

  <svg class="abs laundry" width="80" height="14" viewBox="0 0 80 14" fill="none" stroke="var(--ink-soft)" stroke-width="0.8">
    <path d="M1 3 L3 12 H12 L14 3"/><path d="M1 5 Q4 3 7.5 5 T14 5"/>
    <path d="M18 12 L24 2 L30 12 Z"/><path d="M19 2 L29 12 M29 2 L19 12"/>
    <path d="M34 11 H46 V8 Q46 4 40 4 H36 Z"/>
    <circle cx="56" cy="7" r="5"/><text x="54" y="9.5" font-size="6" fill="var(--ink-soft)" stroke="none" font-family="Quicksand,sans-serif">P</text>
    <rect x="65" y="2" width="10" height="10"/><circle cx="70" cy="7" r="3.5"/>
  </svg>
  <p class="abs origin">Designed in the USA<br>Made in China</p>
  <p class="abs sku">Baby Burp Cloth<br>New</p>

</main>
</body>
</html>
```